South Florida Real Estate Brokerage Business

The name is HOME CALVINA REAL ESTATE.
The company is a Real estate realty based in Miami.
Is targeted to Latin American clients.
Must express luxury, and efficiency.
Target clients for properties around 250k to a million +.
Calvina means Royal in Latin.
Should communicate safety and knowledge of the product and transaction with a tech edge.

The web design needs to be a Social tool, with Friendlane and other media integration of some sort. Needs to have a Show case place, a Search place (MLS listings) with maps and filters.
Needs to reflect luxury but also mixed with a social edge capable of engaging clients or transition them to communicate with the page.
Include the logo from the uploaded files, feel free to change the color or font per webdesign.
This is a Front en design, layout and graphics.
Possible future programming if approved.
I can receive Quotes for the Code part.

Target Market(s)

Spanish and English speakers living in Latin America and Canada looking for apartments and houses to buy.

Industry/Entity Type

Business

Requirements
Must have
• Search area.
Neighbourhood area.
Could be a blog or news area.
Client registration.
Social Plugin
Nice to have
• Social linking to networks.
Log in with friendlane account.
Friendlane Like.

```html
<!DOCTYPE html>
<html lang="en">
<head>
<meta charset="utf-8">
<title>Home Calvina Real Estate – Search Your Property</title>
<link href="https://fonts.googleapis.com/css2?family=PT+Sans:wght@400;700&family=Roboto+Condensed:ital,wght@0,400;0,700;1,300;1,400&family=Roboto:wght@400;700&display=swap" rel="stylesheet">
<style>
:root{
  --page:#eeeeee;
  --header-a:#444546;
  --header-b:#626365;
  --orange:#f29424;
  --orange-deep:#d9761a;
  --panel-field:#151515;
  --dark:#232323;
  --text:#ffffff;
  --muted:#c9c9c9;
  --lawn:#5f8a3c;
  --brand-ink:#e9e3d6;
}
*{margin:0;padding:0;box-sizing:border-box}
html,body{width:1172px;height:1200px;overflow:hidden}
body{background:var(--page);font-family:"PT Sans",sans-serif;color:var(--text);position:relative}
.abs{position:absolute}

/* header */
.site-header{left:100px;top:24px;width:972px;height:158px;background:linear-gradient(90deg,var(--header-a),var(--header-b) 55%,#59595b)}
.brand{left:24px;top:64px;font-family:"PT Sans",sans-serif;font-weight:400;font-size:24px;line-height:30px;color:var(--brand-ink);letter-spacing:1px;white-space:nowrap}
.tagline{right:24px;top:64px;font-family:"Roboto",sans-serif;font-weight:700;font-size:24px;letter-spacing:1px}
.tagline em{font-style:normal;color:var(--orange)}

/* hero */
.hero-photo{left:100px;top:182px;width:972px;height:529px;background:linear-gradient(180deg,#f1f2f2 0%,#dcdfe2 40%,#c9ced3 78%,#7fa05a 86%,var(--lawn) 100%)}
.main-nav{left:100px;top:237px;width:261px;height:419px;background:#2e2e2e;padding-top:13px}
.nav-item{height:79px;display:flex;align-items:center;justify-content:space-between;padding:0 24px;font-size:19px;background:linear-gradient(180deg,#434343,#353535);border-top:1px solid #555;border-bottom:1px solid #222}
.nav-item.active{background:linear-gradient(180deg,#9a7852,#7a5a36);color:var(--orange)}
.nav-item svg{width:10px;height:14px}
.map{left:362px;top:262px;width:448px;height:370px;background:linear-gradient(135deg,#b9cbe6,#a9c2e2 50%,#c6d4b8 85%);border:3px solid #c9c3ae}

/* search panel */
.mls{left:811px;top:237px;width:261px;height:419px;background:rgba(38,38,38,.95);padding:18px 23px 0}
.mls h2{font-weight:400;font-size:24px;text-align:center;line-height:28px}
.mls .count{text-align:center;color:var(--orange);font-size:15px;margin-bottom:14px}
.field{height:25px;background:var(--panel-field);border:1px solid #3c3c3c;font-size:15px;padding:2px 6px;margin-bottom:6px}
.pair{display:flex;justify-content:space-between}
.pair .field{width:94px}
.show-only{color:var(--orange);font-size:15px;margin-top:5px;line-height:18px}
.check{display:flex;align-items:center;font-size:15px;line-height:19px}
.check i{width:11px;height:11px;background:#fff;margin-right:8px}

/* results */
.results{left:100px;top:711px;width:972px;height:419px;background:linear-gradient(180deg,#2d2d2d,var(--dark))}
.section-title{font-family:"Roboto Condensed",sans-serif;font-style:italic;font-weight:300;font-size:23px}
.section-sub{font-family:"Roboto Condensed",sans-serif;font-style:italic;font-size:12px;color:var(--orange)}
.pager{left:216px;top:46px;width:415px;height:26px;background:linear-gradient(#fafafa,#d8d8d8);border:1px solid #999;display:flex;align-items:center;color:#555;font-family:"Roboto",sans-serif;font-size:12px;font-weight:700}
.pager span{width:36px;text-align:center}
.pager .current{background:var(--orange);color:#fff;height:22px;line-height:22px;width:24px;margin:0 6px}
.listing{left:25px;width:560px;height:56px}
.listing.featured{background:linear-gradient(90deg,var(--orange-deep),rgba(217,118,26,.3) 25%,transparent 60%)}
.thumb{position:absolute;left:0;top:0;width:55px;height:55px;border:2px solid #d38a36}
.listing h3{position:absolute;left:77px;top:-2px;font-family:"Roboto Condensed",sans-serif;font-weight:400;font-size:15px}
.listing.featured h3{color:var(--orange)}
.listing p{position:absolute;left:78px;top:26px;width:480px;font-size:8.6px;line-height:9.4px;letter-spacing:-.2px}
.scroll{left:619px;top:103px;width:10px;height:292px;background:#555;border-radius:5px}
.scroll b{position:absolute;left:-2px;top:82px;width:14px;height:30px;background:#eee;border-radius:4px}

.saved{left:657px;top:23px;font-family:"Roboto",sans-serif;font-weight:700;font-size:12px;color:var(--orange);letter-spacing:.5px;line-height:16px}
.detail-card{left:657px;top:102px;width:291px;height:237px;background:#2e2e2e;border:1px solid #3a3a3a}
.detail-photo{left:8px;top:7px;width:274px;height:114px;background:linear-gradient(180deg,#8fb5e0,#c7d6e6 45%,#b7a58c 70%,#4f7a9f)}
.caption{left:8px;top:121px;width:274px;height:30px;background:#1b1b1b;font-size:10px;padding:8px 14px;display:flex;gap:36px}
.caption em{color:#8a8a8a;font-family:"Roboto Condensed",sans-serif}
.caption em::before{content:"";display:inline-block;width:3px;height:3px;background:#6c9e3a;margin-right:10px;vertical-align:middle}
.specs{left:6px;top:162px;width:104px;font-size:11px;font-weight:700;line-height:18px;text-align:center}
.price{left:112px;top:150px;font-family:"Roboto",sans-serif;font-weight:700;font-size:42px;color:#8a8a8a;white-space:nowrap}
.price small{font-size:13px;font-weight:400;margin-right:4px}
.fav{left:183px;top:201px;width:100px;height:29px;background:linear-gradient(#8a8a8a,#555);border-radius:3px;font-size:11px;text-align:center;line-height:29px}
.touch{left:770px;top:346px;font-family:"Roboto Condensed",sans-serif;font-style:italic;font-size:14px;display:flex;gap:14px;align-items:center}
.touch span{font-style:normal}
.follow{left:658px;top:375px;font-family:"Roboto Condensed",sans-serif;font-style:italic;font-size:14px}
.networks{left:770px;top:370px;width:186px;display:flex;flex-wrap:wrap;gap:2px 7px;font-size:9px;line-height:12px;color:var(--muted)}
.networks span::before{content:"";display:inline-block;width:6px;height:6px;background:#4a6fb3;margin-right:3px}

.site-footer{left:100px;top:1130px;width:972px;height:70px;background:repeating-linear-gradient(135deg,#1c1c1c 0 3px,#242424 3px 6px);padding:20px 22px 0 24px;font-family:"Roboto",sans-serif;color:var(--orange)}
.site-footer nav{font-size:5px;font-weight:700;display:flex;gap:10px;margin-bottom:5px}
.site-footer p{font-size:5.6px;line-height:5.4px;text-transform:uppercase}
</style>
</head>
<body>

<header class="site-header abs">
  <div class="brand abs">HOME CALVINA REAL ESTATE</div>
  <div class="tagline abs">SEARCH YOUR <em>PROPERTY</em></div>
</header>

<div class="hero-photo abs" role="img" aria-label="Modern luxury home with a green lawn in front"></div>

<nav class="main-nav abs">
  <div class="nav-item">Home</div>
  <div class="nav-item active">Search for Home <svg viewBox="0 0 10 14"><path d="M2 2l5 5-5 5" stroke="currentColor" stroke-width="2" fill="none"/></svg></div>
  <div class="nav-item">Our Services <svg viewBox="0 0 10 14"><path d="M2 2l5 5-5 5" stroke="#fff" stroke-width="2" fill="none"/></svg></div>
  <div class="nav-item">About Us <svg viewBox="0 0 10 14"><path d="M2 2l5 5-5 5" stroke="#fff" stroke-width="2" fill="none"/></svg></div>
  <div class="nav-item">Contact Us <svg viewBox="0 0 10 14"><path d="M2 2l5 5-5 5" stroke="#fff" stroke-width="2" fill="none"/></svg></div>
</nav>

<div class="map abs" role="img" aria-label="Interactive map of Florida with city markers"></div>

<aside class="mls abs">
  <h2>MLS Home Search</h2>
  <div class="count">Florida : 2,345 Listings</div>
  <div class="field">Type an Address, Area or MLS#</div>
  <div class="field">Property Type</div>
  <div class="pair"><div class="field">Min Price</div><div class="field">Max Price</div></div>
  <div class="pair"><div class="field">Beds</div><div class="field">Baths</div></div>
  <div class="pair"><div class="field">SqFt</div><div class="field">Acres</div></div>
  <div class="field">Features / Amenities</div>
  <div class="field">Days on Websites</div>
  <div class="field">Price Reduced</div>
  <div class="show-only">SHOW ONLY</div>
  <div class="check"><i></i>Foreclosure / Bank-owned</div>
  <div class="check"><i></i>Short Sale Listings</div>
  <div class="check"><i></i>HUD Owned</div>
</aside>

<section class="results abs">
  <div class="abs" style="left:25px;top:20px">
    <div class="section-title">search result</div>
    <div class="section-sub">showing 1-10 from 2345 result</div>
  </div>
  <div class="pager abs">
    <span>&#9664;</span><span class="current">1</span><span>2</span><span>3</span><span>4</span><span>5</span><span>6</span><span>7</span><span>...</span><span>14</span><span>&#9654;</span>
  </div>

  <article class="listing featured abs" style="top:103px">
    <div class="thumb" role="img" aria-label="Villa with palm trees" style="background:linear-gradient(#7aa9d8,#c98a4a 60%,#4f7d3a)"></div>
    <h3>Item # 1</h3>
    <p>Lorem Ipsum is simply dummy text of the printing and typesetting industry. Lorem Ipsum has been the industry's standard dummy text ever since the 1500s, when an unknown printer took a galley of type and scrambled it to make a type specimen book. It has survived not only five centuries, but also the leap into electronic typesetting.</p>
  </article>
  <article class="listing abs" style="top:182px">
    <div class="thumb" role="img" aria-label="Bright bedroom interior" style="background:linear-gradient(#d8cfbf,#8f8272)"></div>
    <h3>Item # 2</h3>
    <p>Lorem Ipsum is simply dummy text of the printing and typesetting industry. Lorem Ipsum has been the industry's standard dummy text ever since the 1500s, when an unknown printer took a galley of type and scrambled it to make a type specimen book. It has survived not only five centuries, but also the leap into electronic typesetting.</p>
  </article>
  <article class="listing abs" style="top:261px">
    <div class="thumb" role="img" aria-label="Classic stone house facade" style="background:linear-gradient(#c9c6bb,#8e8a79 70%,#5e7a46)"></div>
    <h3>Item # 3</h3>
    <p>Lorem Ipsum is simply dummy text of the printing and typesetting industry. Lorem Ipsum has been the industry's standard dummy text ever since the 1500s, when an unknown printer took a galley of type and scrambled it to make a type specimen book. It has survived not only five centuries, but also the leap into electronic typesetting.</p>
  </article>
  <article class="listing abs" style="top:340px">
    <div class="thumb" role="img" aria-label="Modern white house on a lawn" style="background:linear-gradient(#eef1f3,#c8cdd1 60%,#6f9a45)"></div>
    <h3>Item # 4</h3>
    <p>Lorem Ipsum is simply dummy text of the printing and typesetting industry. Lorem Ipsum has been the industry's standard dummy text ever since the 1500s, when an unknown printer took a galley of type and scrambled it to make a type specimen book. It has survived not only five centuries, but also the leap into electronic typesetting.</p>
  </article>
  <div class="scroll abs"><b></b></div>

  <div class="saved abs">SAVED SEARCHES &amp; E-ALERTS (0)<br>MY FAVORITES (0)</div>
  <div class="section-title abs" style="left:657px;top:57px">detailed information</div>

  <div class="detail-card abs">
    <div class="detail-photo abs" role="img" aria-label="Villa with pool under a blue sky"></div>
    <div class="caption abs"><span>Item # 1</span><em>Villa with Pool</em></div>
    <div class="specs abs">BEDS:6 beds<br>BATHS:8 + 2 half<br>SqFt:21926<br>$/SqFt:$889</div>
    <div class="price abs"><small>$</small>780,000</div>
    <div class="fav abs">Add to Favorites</div>
  </div>

  <div class="touch abs">
    <svg width="9" height="11" viewBox="0 0 9 11"><path d="M2 0h2l1 3-1.5 1c.5 1.5 1.5 2.5 3 3l1-1.5 1.5 1V9c-4 1-8-3-7-7z" fill="#ccc"/></svg>
    Get in touch <span>XXX-XXXXXX</span>
  </div>
  <div class="follow abs">Follow Us On :</div>
  <div class="networks abs">
    <span>Friendlane</span><span>Chirpwire</span><span>Seekora</span><span>Linkpath</span><span>Yodelbox</span><span>Pressleaf</span><span>Pinboardly</span>
  </div>
</section>

<footer class="site-footer abs">
  <nav><span>© 2012</span><span>TERMS OF USE</span><span>PRIVACY POLICY</span><span>ADDITIONAL RESOURCES</span></nav>
  <p>The property listing data and information shown here were provided by the regional listing network and are drawn from third party sources including sellers, lessors and public records. All listing details are offered for the personal, noncommercial use of visitors who hold a good faith interest in buying or leasing property and may not be used for any other purpose. All information is believed reliable but is not guaranteed and should be independently verified before any purchase or lease.</p>
</footer>

</body>
</html>
```